Book Cover for Harbor Holiday Voyage Needed!

Amber Hollow Press needs a cover for a novella. We will need an ebook cover and print wrap. We need to stay with the brand we have as indicated by the files attached. Take a look for the brand and style we are looking for.
Here are the specifics:
Title (subject to change): Starlit Passage
Subtitle: A Yuletide Novella
Series Name: The Sunny Shore Love Series (Book 3.5)
Author: Kenna Bellwood

Target Market(s)

Romance readers

Industry/Entity Type

Entertainment Industry

Font styles to use
Other font styles liked:
• NovitoNova - Title, Neumann - Subtitle

Colors
3276b5
33a6d7
33b8a4
abd036
fbee3d
ffc214

Requirements
Must have
• Please take a look at the other three covers to stay on brand and for inspiration
Nice to have
• Possibly something with a criuse ship.
Should not have
• Not looking for "real" images or depictions. We want a scene with bright colors same as the previous books but with a bit of a casual feel.

```html
<!DOCTYPE html>
<html lang="en">
<head>
<meta charset="utf-8">
<title>Starlit Passage – A Yuletide Novella</title>
<link rel="stylesheet" href="https://fonts.googleapis.com/css2?family=Poiret+One&family=Forum&family=Oswald:wght@300&display=swap">
<style>
  :root {
    --page: #ffffff;
    --sky-top: #a9d5ea;
    --sky-mid: #c6e5f1;
    --cloud: #eef7f8;
    --sea-far: #6fbfd9;
    --sea-near: #a9dbe3;
    --foam: #f4f6ee;
    --sand: #efe4bd;
    --title: #dd9a5f;
    --title-shadow: rgba(40, 70, 90, 0.45);
    --green: #3f5f2f;
    --navy: #1f2f4f;
    --banner-a: rgba(250, 245, 235, 0.75);
    --banner-b: rgba(214, 168, 122, 0.85);
    --banner-edge: #d9ae78;
  }
  html, body {
    margin: 0;
    padding: 0;
    width: 1000px;
    height: 1200px;
    overflow: hidden;
    background: var(--page);
  }
  .cover {
    position: absolute;
    left: 124px;
    top: 0;
    width: 776px;
    height: 1200px;
    overflow: hidden;
  }
  .cover-scene {
    position: absolute;
    inset: 0;
    background:
      radial-gradient(ellipse 60% 9% at 30% 690px, var(--cloud), transparent 70%),
      radial-gradient(ellipse 50% 8% at 85% 600px, var(--cloud), transparent 70%),
      linear-gradient(to bottom,
        var(--sky-top) 0px,
        var(--sky-mid) 520px,
        var(--cloud) 700px,
        var(--sea-far) 752px,
        var(--sea-near) 960px,
        var(--foam) 1010px,
        var(--sand) 1060px,
        var(--sand) 1200px);
  }
  .series-banner {
    position: absolute;
    left: 59px;
    top: 52px;
    width: 652px;
    height: 58px;
    box-sizing: border-box;
    border: 2px solid var(--banner-edge);
    background: linear-gradient(to right, var(--banner-a), var(--banner-b));
    display: flex;
    align-items: center;
    justify-content: center;
    font-family: "Forum", serif;
    font-size: 27px;
    letter-spacing: 0.5px;
    color: var(--navy);
    white-space: nowrap;
  }
  .title {
    position: absolute;
    left: 0;
    top: 0;
    width: 776px;
    height: 560px;
  }
  .title text {
    font-family: "Poiret One", sans-serif;
    fill: var(--title);
    filter: drop-shadow(5px 6px 4px var(--title-shadow));
  }
  .subtitle {
    position: absolute;
    left: 0;
    width: 776px;
    top: 562px;
    text-align: center;
    font-family: "Oswald", sans-serif;
    font-weight: 300;
    font-size: 50px;
    letter-spacing: 2px;
    color: var(--green);
    margin: 0;
  }
  .author {
    position: absolute;
    left: 0;
    width: 776px;
    top: 1038px;
    text-align: center;
    font-family: "Forum", serif;
    font-size: 68px;
    line-height: 62px;
    letter-spacing: 2px;
    color: var(--green);
    margin: 0;
  }
</style>
</head>
<body>
  <main class="cover">
    <div class="cover-scene" role="img" aria-label="Bright illustrated beach scene: pale sky with soft clouds, palm fronds at the upper right, a small white sailboat on a calm turquoise sea, and gentle waves on sandy shore"></div>

    <div class="series-banner">THE SUNNY SHORE LOVE SERIES (BOOK 3.5)</div>

    <svg class="title" viewBox="0 0 776 560" aria-label="Starlit Passage">
      <text x="91" y="388" font-size="260" textLength="595" lengthAdjust="spacingAndGlyphs">STARLIT</text>
      <text x="106" y="525" font-size="172" textLength="575" lengthAdjust="spacingAndGlyphs">PASSAGE</text>
    </svg>

    <p class="subtitle">A YULETIDE NOVELLA</p>

    <p class="author">KENNA<br>BELLWOOD</p>
  </main>
</body>
</html>
```